VEXA New York *Luxury Candles*

We need a logo AND package design for a new private label luxury candle company.
I'm an interior decorator. When you enter a space you can perceive design as a 3 dimensional experience. However, the perfect scent in a space makes your experience unforgettable and 4 dimensional. Scents have the power to evoke pleasure and bring back memories.
I want my costumer to have a luxurious experience from the moment they see the package, open it, smell, enjoy and use it to decorate their spaces.
We are looking for a clean design that reads LUX. I'm attaching some pictures for Inspiration.
The candle is approximately 4 inches high 3.5 inches wide (10.3cm high, 9cm wide).

The company's name is

VEXA
New York

Target Market(s)

Women between 27 and 50 who like design, elegance, and beautiful spaces.
They like to indulge and create their safety sanctuary at home.

Industry/Entity Type

It Company

Font styles to use
Sans Serif
Script

Requirements
Must have
• A design for the candle and a design for the gift box + logo
Nice to have
• Simplicity
• Elegance
• Efortless beauty
Should not have
• Many different colors
• Shouldn't be overdone

```html
<!DOCTYPE html>
<html lang="en">
<head>
<meta charset="utf-8">
<title>VEXA New York — Candle Packaging</title>
<link href="https://fonts.googleapis.com/css2?family=Josefin+Sans:wght@300;400&family=Playfair+Display+SC:wght@700&display=swap" rel="stylesheet">
<style>
  :root {
    --backdrop-light: #8e8e8e;
    --backdrop-dark: #5c5c5c;
    --panel: #2f2423;
    --panel-deep: #241b1a;
    --label-top: #ffffff;
    --label-bottom: #ece3d3;
    --ink: #1e1a19;
    --gold: #c9a66b;
    --gold-soft: #b8975f;
    --caption: #ffffff;
  }
  * { box-sizing: border-box; margin: 0; padding: 0; }
  html, body { width: 1200px; height: 907px; overflow: hidden; }
  body {
    position: relative;
    background: radial-gradient(ellipse at 50% 40%, var(--backdrop-light), var(--backdrop-dark));
    font-family: "Josefin Sans", sans-serif;
  }
  .panel {
    position: absolute;
    background: linear-gradient(180deg, var(--panel) 0%, var(--panel-deep) 100%);
  }
  .panel--box-front { left: 300px; top: 60px; width: 300px; height: 400px; }
  .panel--side { left: 817px; top: 27px; width: 355px; height: 392px; }
  .panel--front-option { left: 413px; top: 472px; width: 340px; height: 408px; }
  .panel--top { left: 817px; top: 472px; width: 355px; height: 408px; }

  .label {
    position: absolute;
    background: linear-gradient(180deg, var(--label-top), var(--label-bottom));
    text-align: center;
    color: var(--ink);
  }
  .label::before {
    content: "";
    position: absolute;
    inset: 5px;
    border: 1px solid var(--ink);
  }
  .panel--box-front .label { left: 73px; top: 55px; width: 144px; height: 188px; }
  .panel--side .label { left: 90px; top: 130px; width: 174px; height: 134px; }
  .panel--front-option .label { left: 93px; top: 32px; width: 178px; height: 208px; }

  .brand-name {
    display: block;
    font-weight: 300;
    letter-spacing: 0.3em;
    padding-left: 0.3em;
  }
  .brand-city {
    display: block;
    font-weight: 300;
    letter-spacing: 0.3em;
    padding-left: 0.3em;
  }
  .rule { display: block; margin: 0 auto; height: 1px; background: currentColor; opacity: 0.6; }
  .scent-name { display: block; font-size: 8px; letter-spacing: 0.25em; line-height: 1.5; }

  .panel--box-front .brand-name { font-size: 24px; margin-top: 52px; }
  .panel--box-front .brand-city { font-size: 7px; margin-top: 6px; }
  .panel--box-front .rule { width: 106px; margin-top: 4px; }
  .panel--box-front .scent-name { margin-top: 26px; }

  .panel--side .brand-name { font-size: 26px; margin-top: 42px; }
  .panel--side .brand-city { font-size: 7px; margin-top: 6px; }
  .panel--side .rule { width: 130px; margin-top: 8px; }

  .panel--front-option .brand-name { font-size: 28px; margin-top: 62px; }
  .panel--front-option .brand-city { font-size: 8px; margin-top: 6px; }
  .panel--front-option .rule { width: 126px; margin-top: 4px; }
  .panel--front-option .scent-name { margin-top: 28px; font-size: 9px; }

  .net-weight {
    position: absolute; left: 0; right: 0;
    text-align: center; color: var(--gold);
    line-height: 1.5;
  }
  .net-weight small { display: block; font-size: 7px; color: var(--gold-soft); }
  .net-weight span { font-size: 9px; }
  .panel--box-front .net-weight { bottom: 40px; }
  .panel--front-option .net-weight { bottom: 26px; }
  .panel--front-option .net-weight span { font-size: 10px; }

  .top-mark {
    position: absolute; left: 0; right: 0; top: 186px;
    text-align: center; color: var(--gold);
    font-weight: 300; font-size: 22px; letter-spacing: 0.3em; padding-left: 0.3em;
  }

  .jar-label {
    position: absolute; left: 72px; top: 152px; width: 176px; height: 258px;
    background: var(--panel);
    color: var(--gold);
    text-align: center;
  }
  .jar-label::before {
    content: ""; position: absolute;
    left: 12px; right: 12px; top: 40px; bottom: 42px;
    border: 1px solid var(--gold);
  }
  .jar-label .brand-name { font-size: 22px; margin-top: 108px; }
  .jar-label .brand-city { font-size: 6px; margin-top: 6px; }
  .jar-label .rule { width: 118px; margin-top: 5px; }
  .jar-label .scent-name { margin-top: 24px; font-size: 7px; }

  .caption {
    position: absolute;
    font-family: "Playfair Display SC", serif;
    font-weight: 700;
    color: var(--caption);
    font-size: 28px;
    text-shadow: 1px 2px 2px rgba(0,0,0,0.6);
  }
  .caption--side { left: 965px; top: 428px; }
  .caption--front { left: 220px; top: 834px; font-size: 27px; }
  .caption--top { left: 983px; top: 862px; }
</style>
</head>
<body>
  <div class="jar-label">
    <span class="brand-name">VEXA</span>
    <span class="brand-city">NEW YORK</span>
    <span class="rule"></span>
    <span class="scent-name">SIGNATURE SCENT</span>
  </div>

  <section class="panel panel--box-front">
    <div class="label">
      <span class="brand-name">VEXA</span>
      <span class="brand-city">NEW YORK</span>
      <span class="rule"></span>
      <span class="scent-name">SIGNATURE<br>SCENT</span>
    </div>
    <p class="net-weight"><small>scented candles</small><span>Net.wt. 165g/5.8oz</span></p>
  </section>

  <section class="panel panel--side">
    <div class="label">
      <span class="brand-name">VEXA</span>
      <span class="brand-city">NEW YORK</span>
      <span class="rule"></span>
    </div>
  </section>
  <p class="caption caption--side">Side</p>

  <section class="panel panel--front-option">
    <div class="label">
      <span class="brand-name">VEXA</span>
      <span class="brand-city">NEW YORK</span>
      <span class="rule"></span>
      <span class="scent-name">SIGNATURE<br>SCENT</span>
    </div>
    <p class="net-weight"><small>scented candles</small><span>Net.wt. 165g/5.8oz</span></p>
  </section>
  <p class="caption caption--front">Front option</p>

  <section class="panel panel--top">
    <p class="top-mark">VEXA</p>
  </section>
  <p class="caption caption--top">Top</p>
</body>
</html>
```